Business Card Design

we are a brand new cable TV network devoted to self improvement and leading a better life called FLOURIVO TV.I have a logo. We have 3 executives that need cards.I want it to be a heavy stock card: professional but showing our creative nature

Industry/Entity Type

Business

Contact Information for Business Card

CLAUDIA SAENZ AMLIECEO350 San Juan DrPonte Vedra Beach FL 32082904-473-5953

```html
<!DOCTYPE html>
<html lang="en">
<head>
<meta charset="utf-8">
<title>Business Card</title>
<link href="https://fonts.googleapis.com/css2?family=Nunito:wght@400;700&display=swap" rel="stylesheet">
<style>
  :root {
    --page-bg: #e6e2dc;
    --card-bg: #f4f3f1;
    --card-edge: #dcdad6;
    --brand-red: #d3232a;
    --brand-red-dark: #b51b21;
    --band-dark: #1c1b1b;
    --text-dark: #2a2a2a;
  }
  * { margin: 0; padding: 0; box-sizing: border-box; }
  html, body {
    width: 1200px;
    height: 1200px;
    overflow: hidden;
    background: var(--page-bg);
    font-family: "Nunito", sans-serif;
  }
  .card {
    position: absolute;
    left: 100px;
    top: 304px;
    width: 1000px;
    height: 592px;
    background: var(--card-bg);
    border: 1px solid var(--card-edge);
    border-radius: 14px;
    overflow: hidden;
    box-shadow: 0 10px 30px rgba(0,0,0,0.12);
  }
  .brand {
    position: absolute;
    left: 80px;
    top: 75px;
    width: 330px;
    height: 290px;
    display: flex;
    flex-direction: column;
    justify-content: center;
    align-items: flex-start;
    gap: 14px;
  }
  .brand-dot {
    width: 40px;
    height: 40px;
    border-radius: 50%;
    background: var(--brand-red);
  }
  .brand-name {
    font-size: 46px;
    font-weight: 700;
    line-height: 1;
    color: var(--brand-red);
    letter-spacing: 1px;
    white-space: nowrap;
  }
  .holder {
    position: absolute;
    right: 89px;
    top: 72px;
    text-align: right;
  }
  .holder-name {
    font-size: 29px;
    font-weight: 700;
    line-height: 36px;
    color: var(--brand-red-dark);
  }
  .holder-title {
    margin-top: 4px;
    font-size: 21px;
    font-weight: 400;
    line-height: 26px;
    color: var(--text-dark);
  }
  .contact {
    position: absolute;
    right: 124px;
    top: 396px;
    list-style: none;
    text-align: right;
    font-size: 23px;
    line-height: 33px;
    color: var(--text-dark);
    white-space: nowrap;
  }
  .contact-line { position: relative; }
  .contact-icon {
    position: absolute;
    right: -42px;
    top: 5px;
    width: 22px;
    height: 22px;
  }
  .band {
    position: absolute;
    left: 0;
    bottom: 0;
    width: 1000px;
    height: 52px;
  }
</style>
</head>
<body>
  <div class="card">
    <div class="brand">
      <span class="brand-dot"></span>
      <span class="brand-name">FLOURIVO TV</span>
    </div>

    <div class="holder">
      <p class="holder-name">Mirella Okafor Dunst</p>
      <p class="holder-title">CEO</p>
    </div>

    <ul class="contact">
      <li class="contact-line">904-618-2047
        <svg class="contact-icon" viewBox="0 0 24 24" aria-hidden="true">
          <path fill="#d3232a" d="M3 8c0-2 2-4 9-4s9 2 9 4v2h-5V8H8v2H3z"/>
          <path fill="#d3232a" d="M6 11h12l2 9H4z"/>
          <circle cx="12" cy="15.5" r="2.2" fill="#f4f3f1"/>
        </svg>
      </li>
      <li class="contact-line">718 Harlow Creek Dr Ponte
        <svg class="contact-icon" viewBox="0 0 24 24" aria-hidden="true">
          <path fill="#d3232a" d="M12 2a7 7 0 0 0-7 7c0 5 7 13 7 13s7-8 7-13a7 7 0 0 0-7-7z"/>
          <circle cx="12" cy="9" r="2.6" fill="#f4f3f1"/>
        </svg>
      </li>
      <li class="contact-line">Vedra Beach FL 32097</li>
    </ul>

    <svg class="band" viewBox="0 0 1000 52" preserveAspectRatio="none" aria-hidden="true">
      <path fill="#1c1b1b" d="M0 38 Q500 30 1000 36 L1000 52 L0 52 Z"/>
      <path fill="#d3232a" d="M0 2 Q300 16 560 18 T1000 8 L1000 38 Q500 30 0 40 Z"/>
    </svg>
  </div>
</body>
</html>
```